Moving comapny Postcard mailer Design

I am looking for a 6x9 postcard with real images of our team. I would like to add the same review we currently have , I want the colors of the postcard to be orange and white. I want the team picture to be enlarged with the other pictures to be mimized. I will add example postcards to give rough ideas. My company is called Harlow Moving and the postcards with that name are our current postcards. The additional postcards are from other companies who have better postcards than mine. My goal is for my postcard to be better that theirs.

Target Market(s)

Wealthy people in the 35+ age group

Industry/Entity Type

Moving company

Requirements
Must have
• Beauty

```html
<!DOCTYPE html>
<html lang="en">
<head>
<meta charset="utf-8">
<title>Harlow Moving – Postcard</title>
<link href="https://fonts.googleapis.com/css2?family=Montserrat:ital,wght@0,400;0,600;0,700;0,800;1,400;1,600;1,900&display=swap" rel="stylesheet">
<style>
  :root{
    --orange:#f47a20;
    --orange-deep:#e8650f;
    --grey:#8a8a8a;
    --navy:#0b3a5e;
    --blue:#0a4f7e;
    --blue-light:#0aa0d4;
    --white:#ffffff;
    --ink:#222222;
    --star:#f5c518;
    --page:#ffffff;
  }
  *{box-sizing:border-box;margin:0;padding:0}
  html,body{width:1200px;height:1200px;overflow:hidden;background:var(--page)}
  body{position:relative;font-family:"Montserrat",sans-serif}

  .postcard{
    position:absolute;left:50px;top:233px;width:1100px;height:734px;
    background:var(--white);overflow:hidden;border:1px solid #d8d8d8;
  }

  .team-photo{
    position:absolute;left:380px;top:0;width:720px;height:320px;
    background:linear-gradient(180deg,#8a9a7c 0%,#6f6f68 35%,#a9765a 70%,#e4a07a 88%,rgba(255,255,255,0) 100%);
  }
  .team-photo::after{
    content:"";position:absolute;inset:0;
    background:linear-gradient(90deg,rgba(255,255,255,1) 0%,rgba(255,255,255,0) 22%);
  }

  .headline .band{
    position:absolute;display:flex;align-items:center;justify-content:center;
    font-weight:900;font-style:italic;color:var(--white);
    text-shadow:3px 3px 0 rgba(0,0,0,.22);letter-spacing:-1px;
    box-shadow:6px 6px 0 rgba(0,0,0,.12);
  }
  .band-moving{left:29px;top:53px;width:428px;height:118px;background:var(--orange);transform:rotate(-1.3deg);font-size:84px}
  .band-made{left:94px;top:157px;width:320px;height:76px;background:var(--grey);font-size:70px}
  .band-simple{left:39px;top:237px;width:424px;height:102px;background:var(--orange);transform:rotate(-1deg);font-size:86px}

  .review{position:absolute;left:22px;top:368px;width:388px;text-align:center;color:var(--ink)}
  .review .stars{display:flex;justify-content:center;gap:7px;margin-bottom:6px}
  .review .stars svg{width:26px;height:26px}
  .review p{font-size:13.4px;line-height:18.4px}
  .review .lead{color:var(--orange-deep);font-weight:700}
  .review .thanks{font-style:italic;font-weight:600}

  .offer{
    position:absolute;top:378px;width:207px;height:147px;text-align:center;color:var(--white);
    padding-top:12px;
  }
  .offer-25{left:427px;background:linear-gradient(180deg,var(--orange) 0%,#f68a30 100%);border:2px solid var(--orange-deep)}
  .offer-50{left:651px;background:linear-gradient(135deg,#083a66 0%,var(--blue) 40%,var(--blue-light) 100%);border:2px solid #0b8fd0}
  .offer-100{left:873px;background:linear-gradient(180deg,#f68a30 0%,var(--orange-deep) 100%);border:2px solid var(--orange-deep)}
  .offer .amount{font-size:40px;font-weight:800;line-height:1.1;text-shadow:2px 2px 2px rgba(0,0,0,.3)}
  .offer .terms{font-size:20px;font-weight:700;line-height:27px;margin-top:4px}
  .offer .note{font-size:16px;font-weight:400;margin-top:6px}

  .footer{position:absolute;left:0;top:549px;width:1100px;height:185px;background:var(--navy)}
  .brand-tab{
    position:absolute;left:27px;top:535px;width:226px;height:180px;background:var(--white);
    clip-path:polygon(0 0,100% 0,96% 100%,5% 100%);
    display:flex;align-items:center;justify-content:center;gap:8px;
  }
  .brand-tab .mark{width:16px;height:16px;background:var(--navy);border-radius:50%}
  .brand-tab .name{font-size:19px;font-weight:800;color:var(--navy)}

  .cta{position:absolute;left:300px;width:740px;text-align:center;color:var(--white)}
  .cta-line{top:565px;font-size:34px;font-weight:700}
  .cta-line .free{color:var(--orange)}
  .cta-phone{top:610px;font-size:64px;font-weight:700;display:flex;align-items:center;justify-content:center;gap:16px;letter-spacing:1px}
  .cta-web{top:684px;font-size:29px;font-weight:700;display:flex;align-items:center;justify-content:center;gap:22px}
  .icon{display:inline-block;border-radius:50%;background:var(--orange)}
  .icon svg{display:block}
  .dot-number{position:absolute;right:36px;top:700px;font-size:12.5px;color:var(--white)}
</style>
</head>
<body>
  <article class="postcard">
    <div class="team-photo" role="img" aria-label="Team photo: uniformed moving crew standing in front of an open box truck, with company trucks alongside"></div>

    <h1 class="headline">
      <span class="band band-moving">MOVING</span>
      <span class="band band-made">MADE</span>
      <span class="band band-simple">SIMPLE</span>
    </h1>

    <section class="review">
      <div class="stars" aria-label="Five stars">
        <svg viewBox="0 0 24 24"><polygon fill="#f5c518" points="12,1 15,9 23,9 17,14 19,22 12,17 5,22 7,14 1,9 9,9"/></svg>
        <svg viewBox="0 0 24 24"><polygon fill="#f5c518" points="12,1 15,9 23,9 17,14 19,22 12,17 5,22 7,14 1,9 9,9"/></svg>
        <svg viewBox="0 0 24 24"><polygon fill="#f5c518" points="12,1 15,9 23,9 17,14 19,22 12,17 5,22 7,14 1,9 9,9"/></svg>
        <svg viewBox="0 0 24 24"><polygon fill="#f5c518" points="12,1 15,9 23,9 17,14 19,22 12,17 5,22 7,14 1,9 9,9"/></svg>
        <svg viewBox="0 0 24 24"><polygon fill="#f5c518" points="12,1 15,9 23,9 17,14 19,22 12,17 5,22 7,14 1,9 9,9"/></svg>
      </div>
      <p><span class="lead">This company is incredible!</span> After working all day, they came to our house and without skipping a beat began efficiently moving our heavy household items. They had a great attitude, very friendly, and clearly enjoyed working with each other! They took extremely good care of my household items.<br><span class="thanks">Thank you for a great experience!</span></p>
    </section>

    <div class="offer offer-25"><div class="amount">$25 OFF</div><div class="terms">MOVES UNDER<br>$1000</div><div class="note">With this card.</div></div>
    <div class="offer offer-50"><div class="amount">$50 OFF</div><div class="terms">MOVES UNDER<br>$1000</div><div class="note">With this card.</div></div>
    <div class="offer offer-100"><div class="amount">$100 OFF</div><div class="terms">MOVES UNDER<br>$1000</div><div class="note">With this card.</div></div>

    <footer class="footer"></footer>
    <div class="brand-tab"><span class="mark"></span><span class="name">Harlow Moving</span></div>

    <div class="cta cta-line">Call us today and get a <span class="free">FREE</span> Quote!</div>
    <div class="cta cta-phone">
      <span class="icon"><svg width="36" height="36" viewBox="0 0 36 36"><path fill="#fff" d="M12 9c1-.6 2-.3 2.5.7l1.6 3.2c.4.8.2 1.7-.5 2.2l-1.3 1c1 2.3 2.7 4 5 5l1-1.3c.5-.7 1.4-.9 2.2-.5l3.2 1.6c1 .5 1.3 1.5.7 2.5l-1 1.6c-.7 1.1-2 1.6-3.3 1.3C16.5 24.8 11.2 19.5 9.6 13c-.3-1.3.2-2.6 1.3-3.3z"/></svg></span>
      (865) 555-0142
    </div>
    <div class="cta cta-web">
      <span class="icon"><svg width="30" height="30" viewBox="0 0 30 30"><g fill="none" stroke="#0b3a5e" stroke-width="1.4"><circle cx="15" cy="15" r="8"/><ellipse cx="15" cy="15" rx="3.5" ry="8"/><path d="M7 15h16M8.5 11h13M8.5 19h13"/></g></svg></span>
      www.harlowmovers.com
    </div>
    <div class="dot-number">DOT # 4820175</div>
  </article>
</body>
</html>
```